Social Media Tool / Marketing Tool homepage design

We need a design template for a website to promote a web based technology / service. The product provide companies with a tools to generate business from social media web site.

We would like a homepage designed and an inner page of the site. This can be a contact us page or a sign up screen... Would also be good to have a design for the blog page of the site and static page i.e affiliates or advertiser page.

The feel of the site should reflect the fact that this is a social media tool but should not be too casual as we will have business clients so a blend between informal, practical and should communicate to business people (professional marketers)

Site should look friendly, thinking rounded edges rather than squared.

We have included logo design and like the idea of using the haxagonal shapes on the background in some way... Also included link to black on black design mock up that's not right as it's too heavy and does not appeal to any of the women we have shown it to. (50% of our audience)

http://mockups.brindlevault-studio.example/ORB/showcase/html/mockup3.html

http://mockups.brindlevault-studio.example/ORB/showcase/html/mockup1_2.html

http://mockups.brindlevault-studio.example/ORB/showcase/html/inner-page1.html

Above link to design that's not right. The taxonomy is right just not the black on black design. We are happy to use black but not black on a black background.

Please consider that we have 4 user types we are trying to sell to on this page hence the 4 blocks on the homepage. Feel free to interparate this how you will could be good as hexagons? or blocks??

Have attached a powerpoint of site pages please take homepage and dummy content and sign up / form page or contact page.

I have also attached logos please only use logo with one coloured hexagon the other file (logo) does not have the hexagon coloured but does include a set of icons that could also be used.

logo font = Metrostyle extended

Target Market(s)

Young professional marketers at bluechip businesses. User of social media sites like pormbly / quillnest and chirvo.

Industry/Entity Type

Business

Requirements
Must have
• should include pormbly, chirvo and quillnest icons (these will link to our profiles on these sites) Should feel friendly yet established, should feel social as this is a tool to market via social media. rounded edges / corners.
Should not have
• not old style fonts not fonts like times roman .. no squared (hard) corners.

```html
<!DOCTYPE html>
<html lang="en">
<head>
<meta charset="utf-8">
<title>Orbimetra – Home</title>
<link rel="stylesheet" href="https://fonts.googleapis.com/css2?family=Didact+Gothic&family=Arimo:wght@400;700&display=swap">
<style>
:root{
  --ink:#0b0b0b;
  --panel:#111111;
  --panel-line:#2a2a2a;
  --orange:#ff6a00;
  --orange-light:#ff8a1e;
  --white:#ffffff;
  --muted:#9a9a9a;
  --field:#3a3a3a;
  --text-dark:#111111;
  --blue:#1aa4e8;
  --magenta:#e0208c;
  --pink:#f04aa0;
  --green:#3bb54a;
}
*{box-sizing:border-box;margin:0;padding:0}
html,body{width:1200px;height:922px;overflow:hidden}
body{
  position:relative;
  font-family:"Arimo",Arial,sans-serif;
  color:var(--white);
  background:
    radial-gradient(ellipse 520px 420px at 80px 860px,#13c2f0 0%,rgba(19,194,240,0) 100%),
    radial-gradient(ellipse 420px 520px at 1180px 760px,#2fc04a 0%,rgba(47,192,74,0) 100%),
    radial-gradient(ellipse 380px 360px at 1000px 480px,#f08a1a 0%,rgba(240,138,26,0) 100%),
    linear-gradient(100deg,#7a4fd6 0%,#c040c8 30%,#e6248f 55%,#d7207a 72%,#e85b2e 88%,#4aaa3a 100%);
}
.panel{position:absolute;background:var(--panel);border-radius:6px}
.head{left:28px;top:7px;width:1138px;height:65px}
.brand{position:absolute;display:flex;align-items:center;gap:8px;
  font-family:"Didact Gothic",sans-serif;font-size:30px;color:var(--white);letter-spacing:.5px}
.brand .dot{width:22px;height:22px;border-radius:50%;background:var(--orange)}
.head .brand{left:18px;top:14px}
.nav{position:absolute;left:356px;top:0;height:65px;display:flex;list-style:none}
.nav li{font-family:"Didact Gothic",sans-serif;font-size:19px;line-height:65px;margin-right:33px;color:var(--white)}
.nav li.home{border-top:3px solid var(--magenta);border-bottom:3px solid var(--magenta);line-height:59px;padding:0 10px;margin-left:-10px;margin-right:23px}
.nav li.active{color:var(--orange);text-decoration:underline}

.hero{position:absolute;left:28px;top:82px;width:754px;height:182px;border-radius:6px;
  background:linear-gradient(90deg,rgba(180,170,235,.55),rgba(240,150,210,.5));overflow:hidden}
.hero .portrait{position:absolute;left:12px;top:0;width:110px;height:150px;
  background:linear-gradient(180deg,#c9d6ea,#4b86c9)}
.hero blockquote{position:absolute;left:135px;top:22px;width:590px;
  font-family:"Didact Gothic",sans-serif;font-size:29px;line-height:37px;color:var(--text-dark)}
.hero .credit{position:absolute;left:0;bottom:0;width:100%;height:33px;background:var(--ink);
  display:flex;justify-content:space-between;align-items:center;padding:0 12px 0 18px}
.hero .name{font-family:"Didact Gothic",sans-serif;font-size:16px}
.hero .count{font-size:13px;color:var(--orange)}
.hero .count b{color:var(--orange-light)}

.card{position:absolute;width:374px;height:263px;border-radius:6px;overflow:hidden}
.card.blue{background:linear-gradient(90deg,rgba(150,180,240,.55),rgba(210,160,235,.5))}
.card.pink{background:linear-gradient(90deg,rgba(240,140,210,.55),rgba(245,160,190,.5))}
.card h2{position:absolute;left:16px;top:6px;font-family:"Didact Gothic",sans-serif;font-weight:400;
  font-size:37px;color:var(--text-dark);letter-spacing:.5px}
.card .rule{position:absolute;left:8px;right:8px;top:50px;height:6px;
  background:linear-gradient(90deg,#3a6ad0,#8a3ec0)}
.card.pink .rule{background:linear-gradient(90deg,#b01c8a,#e0207a)}
.card ul{position:absolute;left:20px;top:74px;width:330px;list-style:none}
.card li{position:relative;padding-left:34px;font-size:16.5px;line-height:20px;color:var(--text-dark);margin-bottom:16px}
.card li::before{content:"";position:absolute;left:0;top:5px;border-left:8px solid var(--text-dark);
  border-top:5px solid transparent;border-bottom:5px solid transparent}
.card .foot{position:absolute;left:0;bottom:0;width:100%;height:57px;background:var(--ink)}
.btn{position:absolute;display:flex;align-items:center;justify-content:space-between;
  background:linear-gradient(180deg,var(--orange-light),var(--orange));border-radius:5px;
  color:var(--white);font-weight:700;font-size:14px;padding:0 10px 0 9px}
.btn::after{content:"";border-left:9px solid var(--white);border-top:6px solid transparent;border-bottom:6px solid transparent}
.card .btn{right:20px;top:14px;width:126px;height:29px}

.login{left:792px;top:80px;width:374px;height:74px}
.field{position:absolute;height:27px;border-radius:5px;background:var(--field);border:1px solid #555;
  color:#bbb;font-size:13px;line-height:25px;padding-left:8px}
.login .btn{left:276px;top:11px;width:89px;height:27px}
.login .forgot{position:absolute;left:10px;top:52px;font-size:13px;color:var(--muted)}
.login .forgot b{color:var(--orange)}
.login .sep{position:absolute;left:10px;right:10px;top:44px;height:1px;background:var(--panel-line)}

.about{left:792px;top:162px;width:374px;height:468px;padding:18px 10px 0 14px}
.about .brand{position:static;font-size:32px}
.about .lead{font-size:12.5px;margin-top:14px}
.about .big{font-size:23px;line-height:24px;padding-bottom:6px;border-bottom:1px solid #555}
.about .via{font-size:12.5px;color:var(--orange);margin-top:10px}
.about .orange-big{font-size:23px;line-height:22px;color:var(--orange)}
.about p{font-size:12.5px;line-height:16px;margin-top:12px;text-align:justify}
.about ul{list-style:none;margin-top:14px;padding-left:12px}
.about li{position:relative;padding-left:24px;font-size:12.5px;line-height:16px;margin-bottom:17px;text-align:justify}
.about li::before{content:"";position:absolute;left:0;top:2px;border-left:8px solid var(--orange);
  border-top:6px solid transparent;border-bottom:6px solid transparent}
.about .btn{left:19px;top:416px;width:126px;height:28px}

.news{left:792px;top:638px;width:374px;height:86px}
.news h3{position:absolute;left:14px;top:12px;font-weight:400;font-size:16.5px}
.news .btn{left:236px;top:43px;width:126px;height:28px}

.follow{left:792px;top:732px;width:374px;height:73px}
.follow h3{position:absolute;left:16px;top:28px;font-weight:400;font-size:16.5px}
.social{position:absolute;top:19px;width:34px;height:34px;border-radius:7px;display:block}
.social.qn{background:linear-gradient(180deg,#6e8fd6,#2f5aa8)}
.social.ch{background:linear-gradient(180deg,#9ee6f8,#3ab7e3)}

.footer{left:28px;top:812px;width:1138px;height:38px;font-size:12.5px;color:#ddd;
  display:flex;justify-content:space-between;align-items:center;padding:0 14px}
.footer nav span{margin:0 7px}
</style>
</head>
<body>

<header class="panel head">
  <div class="brand"><span>Orbimetra</span><span class="dot"></span></div>
  <ul class="nav">
    <li class="home">HOME</li>
    <li>WHAT?</li>
    <li>WHY?</li>
    <li class="active">DEMO</li>
    <li>REPORTS</li>
    <li>BLOG</li>
    <li>PRICING</li>
    <li>CONTACT</li>
  </ul>
</header>

<section class="hero">
  <div class="portrait" role="img" aria-label="Photo of a smiling businessman in a blue shirt, arms crossed"></div>
  <blockquote>“It’s very easy and fast way to organise campaigns. This tool is something new in my work and I like it!”</blockquote>
  <div class="credit">
    <span class="name">Martin Colby, “Zentrova”</span>
    <span class="count">WE HAVE <b>2358</b> USERS</span>
  </div>
</section>

<section class="card blue" style="left:28px;top:272px">
  <h2>ADVERTISERS</h2><div class="rule"></div>
  <ul><li>Create polls and survey</li><li>Create competitions</li><li>Create B2B and B2C demand generation campaigns</li></ul>
  <div class="foot"><span class="btn">REGISTER</span></div>
</section>
<section class="card pink" style="left:408px;top:272px">
  <h2>ADVOCATES</h2><div class="rule"></div>
  <ul><li>Choose from both B2B and B2C campaigns</li><li>Paid per Lead</li><li>Full marketing tool kit</li></ul>
  <div class="foot"><span class="btn">REGISTER</span></div>
</section>
<section class="card blue" style="left:28px;top:542px">
  <h2>AFFILIATES</h2><div class="rule"></div>
  <ul><li>Create polls and survey</li><li>Create competitions</li><li>Create B2B and B2C demand generation campaigns</li></ul>
  <div class="foot"><span class="btn">REGISTER</span></div>
</section>
<section class="card pink" style="left:408px;top:542px">
  <h2>AGENCIES</h2><div class="rule"></div>
  <ul><li>Choose from both B2B and B2C campaigns</li><li>Paid per Lead</li><li>Full marketing tool kit</li></ul>
  <div class="foot"><span class="btn">REGISTER</span></div>
</section>

<aside class="panel login">
  <div class="field" style="left:10px;top:11px;width:127px">Member Login</div>
  <div class="field" style="left:143px;top:11px;width:127px">Password</div>
  <span class="btn">LOGIN</span>
  <div class="sep"></div>
  <div class="forgot">Forgot Your password? | Not a member? <b>SIGN UP!</b></div>
</aside>

<aside class="panel about">
  <div class="brand"><span>Orbimetra</span><span class="dot"></span></div>
  <div class="lead">It’s a Demand Generation, Social Engagement and</div>
  <div class="big">Advocacy Marketing Platform</div>
  <div class="via">Generate Lead via</div>
  <div class="orange-big">Social Media Email and<br>Our Publisher Network...</div>
  <p>Orbimetra is a platform that allows advertisers to easily create surveys and lead generation campaigns and publish them across the social web.</p>
  <ul>
    <li>Create branded campaign landing pages without involving IT or any technical skills</li>
    <li>Engage with your audience on the social web, survey them for insights</li>
    <li>Generate leads from quillnest, chirvo and pormbly</li>
    <li>Reduce your cycle by providing Your</li>
  </ul>
  <span class="btn">READ MORE</span>
</aside>

<aside class="panel news">
  <h3>Subscribe for newsletter</h3>
  <div class="field" style="left:14px;top:43px;width:211px">Enter Your e-mail</div>
  <span class="btn">SUBSCRIBE</span>
</aside>

<aside class="panel follow">
  <h3>Follow Us</h3>
  <a class="social qn" style="left:138px" aria-label="quillnest"></a>
  <a class="social ch" style="left:194px" aria-label="chirvo"></a>
  <a class="social qn" style="left:252px" aria-label="quillnest"></a>
  <a class="social ch" style="left:309px" aria-label="chirvo"></a>
</aside>

<footer class="panel footer">
  <nav>About Us<span>|</span>Contact Us<span>|</span>Sitemap<span>|</span>Privacy Policy</nav>
  <div>(C) 2011. Orbimetra.example. All rights reserved.</div>
</footer>

</body>
</html>
```